Fleuro-Kanta (Info Flyer for Workshops)

We need a flyer for an event (format A5, double-sided, portrait format). This event is aimed at lymphology experts (for example, pyhsiotherapists and lymphology therapists). The aim of these workshops is to create a quality circle. The logos of the flyer must be as follows: Page 1: with the text and the details of the logotype The logos for the Partners are thus attached below. The following design inputs: 1) The colors black and red (RGB Black: 0/0/0 // RGB Red: 227/0/11 2627) is the corporate color and must be integrated in the flyer. 2) The visual language should be applied to the theme of networking (No Go people, very much using graphical elements.) Please use the graphic element attached below (please use elements of the lymphology pathways, you can change the color into red or / and black. - do not use the whole Body contours (File: lymph2.psd)) 3) The company typeface is Univers LT Std. 4) The texts must be reader-friendly Please note this flyer is not created for Tervalo, but for FleuroKanta ,

```html
<!DOCTYPE html>
<html lang="fr">
<head>
<meta charset="utf-8">
<title>Fleuro-Kanta – Cercle de Qualité</title>
<link href="https://fonts.googleapis.com/css2?family=Roboto+Condensed:wght@400;700;900&family=Lato:wght@400;700&display=swap" rel="stylesheet">
<style>
:root{
  --red:#e3000b;
  --black:#000;
  --ink:#1a1a1a;
  --navy:#0d1f45;
  --bg:#ececec;
  --paper:#fff;
  --grey:#c9c9c9;
}
*{box-sizing:border-box;margin:0;padding:0}
html,body{width:1200px;height:1200px;overflow:hidden}
body{background:var(--bg);position:relative;font-family:"Lato",sans-serif;color:var(--ink)}
.page{position:absolute;top:222px;width:540px;height:757px;background:var(--paper);overflow:hidden;box-shadow:0 4px 12px rgba(0,0,0,.25)}
.page--front{left:38px;background:linear-gradient(#fff 0%,#f4f4f4 60%,#e9e9e9 100%)}
.page--back{left:618px}
.layer{position:absolute;left:0;top:0}
.photo{position:absolute;left:0;top:40px;width:540px;height:360px;background:radial-gradient(ellipse at 50% 60%,#e8edf2 0%,#d4dce4 55%,#f2f2f2 100%)}
.network{position:absolute;left:0;top:0;width:540px;height:170px;background:radial-gradient(ellipse at 50% 20%,#dcdcdc 0%,#f4f4f4 70%,#fff 100%)}
.brand{position:absolute;border-radius:50%;background:#fff;border:4px solid var(--red);display:flex;flex-direction:column;align-items:center;justify-content:center;font-family:"Roboto Condensed",sans-serif;font-weight:700;color:var(--black);line-height:.95;text-transform:uppercase}
.brand--front{left:203px;top:314px;width:136px;height:136px;font-size:24px}
.brand--back{left:217px;top:70px;width:104px;height:104px;font-size:18px}
.headline{position:absolute;left:0;width:100%;text-align:center;font-family:"Roboto Condensed",sans-serif;line-height:1}
.headline--top{top:462px;font-size:62px;font-weight:400;color:var(--black)}
.headline--main{top:528px;font-size:88px;font-weight:900;color:var(--red);letter-spacing:-1px}
.date-pill{position:absolute;left:166px;top:625px;width:210px;height:52px;border:2px solid var(--red);border-radius:26px;display:flex;align-items:center;justify-content:center;font-family:"Roboto Condensed",sans-serif;font-size:32px;color:var(--black)}
.date-pill::before,.date-pill::after{content:"";position:absolute;top:18px;width:14px;height:14px;border-radius:50%;background:var(--red)}
.date-pill::before{left:-7px}.date-pill::after{right:-7px}
.url{position:absolute;left:0;width:100%;top:720px;text-align:center;font-size:14px;letter-spacing:5px;color:var(--red)}
.info{position:absolute;left:0;width:100%;text-align:center}
.label{font-family:"Roboto Condensed",sans-serif;font-size:15px;color:var(--black);line-height:1}
.label::before{content:"— "}.label::after{content:" —"}
.value{color:var(--red);font-size:15px;line-height:1.2}
.value--big{font-size:22px;font-weight:700}
.value--price{font-size:20px;line-height:1.2}
.note{font-size:11px;color:var(--ink)}
.programme{position:absolute;left:54px;width:432px;top:422px;font-size:14px;line-height:1.3;text-align:justify;text-align-last:center}
.partners-title{position:absolute;left:20px;top:677px;font-family:"Roboto Condensed",sans-serif;font-size:11px;font-weight:700}
.partners{position:absolute;left:20px;right:22px;top:692px;height:48px;display:flex;align-items:center;justify-content:space-between;font-size:15px;font-weight:700;color:var(--ink)}
.partner{display:flex;align-items:center;gap:5px}
.partner-dot{width:9px;height:9px;background:var(--navy)}
</style>
</head>
<body>

<section class="page page--front">
  <div class="photo" role="img" aria-label="Photo de groupe de cinq professionnels de santé en blouse blanche"></div>
  <svg class="layer" width="540" height="757" viewBox="0 0 540 757" aria-hidden="true">
    <path d="M0,190 Q270,560 540,190 L540,206 Q270,590 0,206 Z" fill="var(--black)"/>
    <path d="M0,160 Q270,530 540,160 L540,186 Q270,570 0,186 Z" fill="var(--red)"/>
    <path d="M0,400 L0,196 Q270,585 540,196 L540,400 Z" fill="#f1f1f1" opacity="0"/>
    <circle cx="67" cy="302" r="31" fill="#d6d6d6" stroke="var(--red)" stroke-width="4"/>
    <circle cx="475" cy="302" r="31" fill="#d6d6d6" stroke="var(--red)" stroke-width="4"/>
  </svg>
  <div class="brand brand--front"><span>Fleuro</span><span>Kanta</span></div>
  <h1 class="headline headline--top">CERCLE DE</h1>
  <h2 class="headline headline--main">QUALITÉ</h2>
  <div class="date-pill">21 AVRIL 2018</div>
  <p class="url">www.fleurokanta.ch</p>
</section>

<section class="page page--back">
  <div class="network" role="img" aria-label="Réseau de sphères métalliques reliées par des lignes"></div>
  <svg class="layer" width="540" height="200" viewBox="0 0 540 200" aria-hidden="true">
    <path d="M0,0 Q270,290 540,0 L540,14 Q270,310 0,14 Z" fill="var(--black)"/>
    <path d="M20,0 Q270,260 520,0 L540,0 Q270,285 0,0 Z" fill="var(--red)"/>
    <circle cx="64" cy="40" r="31" fill="#d6d6d6" stroke="var(--red)" stroke-width="4"/>
    <circle cx="472" cy="40" r="31" fill="#d6d6d6" stroke="var(--red)" stroke-width="4"/>
  </svg>
  <div class="brand brand--back"><span>Fleuro</span><span>Kanta</span></div>

  <div class="info" style="top:184px"><p class="label">DATE</p></div>
  <div class="info" style="top:207px"><p class="value value--big">21 AVRIL 2018</p></div>
  <div class="info" style="top:246px"><p class="label">HORAIRE</p><p class="value">9H00 - 14H00</p></div>
  <div class="info" style="top:295px"><p class="label">LIEU</p><p class="value" style="margin-top:2px">Auditoire Morel Varin (PMS) CHRV, Lausanne</p></div>
  <div class="info" style="top:350px"><p class="label">DESTINATEUR</p><p class="value" style="margin-top:2px">Physiothérapeutes, Lymphothérapeute</p></div>
  <div class="info" style="top:396px"><p class="label" style="color:var(--red)">PROGRAMME</p></div>
  <p class="programme">après une introduction sur les actualités dans la prise en charge des pathologies lymphatique nous organisons des ateliers pratique (drainage, bandage, compression élastique, les outils etc.)</p>
  <div class="info" style="top:484px"><p class="label">PRIX</p><p class="value value--price">CHF 100</p><p class="value value--price">CHF 50</p><p class="note" style="margin-top:-4px">(pour les membres de FleuroKanta)</p></div>
  <div class="info" style="top:574px"><p class="label">Inscription et renseignement via email</p><p class="value" style="font-size:13px;margin-top:4px">✉ info@fleurokanta.ch</p></div>
  <div class="info" style="top:626px"><p class="label">Délai d’inscription</p><p class="value" style="font-weight:700;margin-top:4px">15 MARS 2018</p><p class="value" style="font-size:11px">(limitation de place, max 80 participants)</p></div>

  <p class="partners-title">Partenairs :</p>
  <div class="partners">
    <span class="partner">Tervalo</span>
    <span class="partner">Norvelle</span>
    <span class="partner">Halden &amp; Moritz</span>
    <span class="partner"><i class="partner-dot"></i>Kestrona</span>
  </div>
</section>

</body>
</html>
```